business card with 2 locations on 1 card

I need a modern looking business card that I would use at 2 different locations. Possibly 1 location on 1 side and other location on other side. One should be able to distinguish the 2 locations immediately before having to read the address or description on card. You can take a look at my website to see what I'm drawn to. The logo is brand new that I just purchased on Craft Hive. I want to emphasize family.
Updates

Let's not use the yellow and blue colors. Added Thursday, August 31, 2017

Target Market(s)

women and children

Industry/Entity Type

Health And Wellness

Contact Information for Business Card

Business name: Willow Brook Chiropractic & Acupuncture
My name: Lorin Daske
Job title: DC, MAOM, LAc (CA), CNS

Location 1
Address: 4817 Marlowe Blvd, Suite B-100, Frisco, TX 75034
Phone: (469) 555-0182
Fax: (972) 555-0137

Location 2
Address: 1936 Belvane Road, Suite 100, Plano, TX 75075
Phone: (469) 555-0169
Fax: (972) 555-0137

Email: drlorindaske@mailnest.example
Website: www.drlorindaske.example

Font styles to use
Serif
Sans Serif

Colors

Designer to choose colors to be used in the design.

Requirements
Must have
• distinction between 2 locations.
Nice to have
• Colors preference below is there. But I like to see what you come up with too!

```html
<!DOCTYPE html>
<html lang="en">
<head>
<meta charset="UTF-8">
<title>Willow Brook Chiropractic &amp; Acupuncture — Business Card</title>
<link rel="stylesheet" href="https://fonts.googleapis.com/css2?family=Cabin:wght@400;500;600&display=swap">
<style>
  :root {
    --page-bg: #d6d6d6;
    --card-white: #f1f1f1;
    --card-white-top: #fafafa;
    --teal: #2f6b68;
    --teal-dark: #2a5f5c;
    --leaf-green: #3aa15a;
    --ink: #3a3a3a;
    --back-top: #a6c68c;
    --back-mid: #7fa882;
    --back-bottom: #426f6b;
    --back-text: #f4f6f2;
  }
  * { box-sizing: border-box; margin: 0; padding: 0; }
  html, body {
    width: 1200px; height: 720px; overflow: hidden;
    background: var(--page-bg);
    font-family: "Cabin", Arial, sans-serif;
  }
  .stage {
    position: relative; width: 1200px; height: 720px;
  }
  .card {
    position: absolute; top: 243px;
    width: 502px; height: 288px;
    box-shadow: 0 2px 5px rgba(0,0,0,0.35);
  }
  .card--front {
    left: 89px;
    background: linear-gradient(180deg, var(--card-white-top), var(--card-white));
  }
  .card--back { left: 625px; overflow: hidden; }

  /* front: holder */
  .holder {
    position: absolute; left: 22px; top: 17px;
    border-left: 8px solid var(--teal);
    padding-left: 6px;
  }
  .holder__name { font-size: 22px; color: var(--ink); line-height: 26px; font-weight: 400; }
  .holder__title { font-size: 13px; color: var(--leaf-green); line-height: 14px; }

  /* front: brand */
  .brand {
    position: absolute; right: 24px; top: 14px;
    width: 150px; text-align: center;
  }
  .brand__circle {
    display: block; margin: 0 auto 6px;
    width: 74px; height: 74px; border-radius: 50%;
    border: 4px solid var(--teal);
  }
  .brand__name {
    font-size: 12px; font-weight: 600; color: var(--teal);
    line-height: 14px; letter-spacing: 0.5px; text-transform: uppercase;
  }

  /* front: contacts */
  .location {
    position: absolute; top: 174px;
    font-size: 13.5px; color: var(--ink); line-height: 16px;
    list-style: none;
  }
  .location--frisco { left: 22px; }
  .location--plano { right: 42px; text-align: right; }
  .location li { display: flex; align-items: flex-start; gap: 9px; margin-bottom: 8px; }
  .location li.location__phone, .location li.location__fax { margin-bottom: 8px; }
  .location--plano li { flex-direction: row-reverse; }
  .location li.location__address { margin-bottom: 11px; }
  .icon { width: 14px; height: 14px; flex: none; fill: var(--teal); margin-top: 1px; }

  /* back */
  .back__field {
    position: absolute; inset: 0;
    background: linear-gradient(180deg, var(--back-top) 0%, var(--back-mid) 50%, var(--back-bottom) 100%);
  }
  .back__motif {
    position: absolute; left: 0; top: 20px; width: 210px; height: 268px;
    background: radial-gradient(ellipse at 35% 45%, rgba(255,255,255,0.16), rgba(255,255,255,0) 70%);
  }
  .back__brand {
    position: absolute; left: 0; right: 0; top: 38px; text-align: center;
    color: var(--back-text);
  }
  .back__circle {
    display: block; margin: 0 0 12px 194px;
    width: 134px; height: 134px; border-radius: 50%;
    border: 4px solid var(--back-text);
  }
  .back__name {
    margin-left: 128px; width: 264px;
    font-size: 17px; font-weight: 500; line-height: 20px;
    letter-spacing: 1px; text-transform: uppercase;
  }
  .back__web {
    position: absolute; left: 128px; width: 264px; top: 244px;
    text-align: center; font-size: 13.5px; color: var(--back-text);
  }
</style>
</head>
<body>
<main class="stage">

  <section class="card card--front" aria-label="Business card front">
    <div class="holder">
      <p class="holder__name">Tomas Reyne</p>
      <p class="holder__title">Director</p>
    </div>

    <div class="brand">
      <span class="brand__circle"></span>
      <p class="brand__name">Willow Brook Chiropractic &amp; Acupuncture</p>
    </div>

    <svg width="0" height="0" style="position:absolute">
      <defs>
        <symbol id="i-pin" viewBox="0 0 24 24"><path d="M12 1a8 8 0 0 0-8 8c0 6 8 14 8 14s8-8 8-14a8 8 0 0 0-8-8zm0 11a3 3 0 1 1 0-6 3 3 0 0 1 0 6z"/></symbol>
        <symbol id="i-phone" viewBox="0 0 24 24"><path d="M2 9c0-3 4-5 10-5s10 2 10 5v2h-5V8.5c-1.5-.5-3-.7-5-.7s-3.5.2-5 .7V11H2zM6 12l3-3h6l3 3v8H6zm6 2a2.5 2.5 0 1 0 0 5 2.5 2.5 0 0 0 0-5z"/></symbol>
        <symbol id="i-fax" viewBox="0 0 24 24"><path d="M7 2h8l3 3v5H7zM2 11h20v10H2zm3 3v2h3v-2zm6 0v2h3v-2zm6 0v2h3v-2z"/></symbol>
        <symbol id="i-mail" viewBox="0 0 24 24"><path d="M2 5h20v14H2zm2 2v.5l8 5.5 8-5.5V7z"/></symbol>
      </defs>
    </svg>

    <ul class="location location--frisco">
      <li class="location__address"><svg class="icon"><use href="#i-pin"/></svg><span>4817 Marlowe Blvd,<br>Suite B-100, Frisco, TX 75034</span></li>
      <li class="location__phone"><svg class="icon"><use href="#i-phone"/></svg><span>(469) 555-0182</span></li>
      <li class="location__fax"><svg class="icon"><use href="#i-fax"/></svg><span>(972) 555-0137</span></li>
      <li class="location__email"><svg class="icon"><use href="#i-mail"/></svg><span>drlorindaske@mailnest.example</span></li>
    </ul>

    <ul class="location location--plano">
      <li class="location__address"><svg class="icon"><use href="#i-pin"/></svg><span>1936 Belvane Road, Suite 100<br>Plano, TX 75075</span></li>
      <li class="location__phone"><svg class="icon"><use href="#i-phone"/></svg><span>(469) 555-0169</span></li>
      <li class="location__fax"><svg class="icon"><use href="#i-fax"/></svg><span>(972) 555-0137</span></li>
      <li class="location__email"><svg class="icon"><use href="#i-mail"/></svg><span>drlorindaske@mailnest.example</span></li>
    </ul>
  </section>

  <section class="card card--back" aria-label="Business card back">
    <div class="back__field"></div>
    <div class="back__motif" role="img" aria-label="Faint decorative tree and leaf pattern"></div>
    <div class="back__brand">
      <span class="back__circle"></span>
      <p class="back__name">Willow Brook Chiropractic &amp; Acupuncture</p>
    </div>
    <p class="back__web">www.drlorindaske.example</p>
  </section>

</main>
</body>
</html>
```